DMB - Stationery Design Project

We need stationery based on our logo.

Company info :
Cabinet Durvaux & Associés
Société à responsabilité limitée au capital de 200.000 FCFP
RCS Papeete 58207K - Numéro tahiti K63095
Centre d’affaires OPALE - Rue Gaston Verdier
BP 51839 MAHANA KOLO - 98713 Papeete
Tahiti - Polynésie française
Tél : +689 40 73 16 84
Fax : +689 40 39 57 61

Industry/Entity Type

It Company

Font styles to use
Sans Serif

```html
<!DOCTYPE html>
<html lang="fr">
<head>
<meta charset="utf-8">
<title>DMB – Papier à en-tête</title>
<link href="https://fonts.googleapis.com/css2?family=Didact+Gothic&display=swap" rel="stylesheet">
<style>
  :root {
    --navy: #1b3a5c;
    --slate: #8c9699;
    --ink: #2b4766;
    --muted: #6f7a80;
    --paper: #ffffff;
    --backdrop: #eceeee;
  }
  * { box-sizing: border-box; margin: 0; padding: 0; }
  html, body {
    width: 1200px;
    height: 936px;
    overflow: hidden;
    background: var(--backdrop);
    font-family: "Didact Gothic", sans-serif;
  }
  .letterhead {
    position: absolute;
    left: 300px;
    top: 44px;
    width: 600px;
    height: 848px;
    background: var(--paper);
    box-shadow: 0 2px 10px rgba(0,0,0,0.08);
    overflow: hidden;
  }
  .brand {
    position: absolute;
    left: 48px;
    top: 52px;
    color: var(--ink);
  }
  .brand-mark {
    display: flex;
    align-items: center;
    gap: 10px;
  }
  .brand-dot {
    width: 12px;
    height: 12px;
    border-radius: 50%;
    background: var(--slate);
  }
  .brand-name {
    font-size: 52px;
    line-height: 1;
    letter-spacing: 1px;
    color: var(--navy);
  }
  .brand-firm {
    margin-top: 4px;
    font-size: 15px;
    color: var(--navy);
  }
  .brand-tagline {
    font-size: 8px;
    color: var(--muted);
    letter-spacing: 0.3px;
  }
  .contact {
    position: absolute;
    right: 40px;
    top: 50px;
    font-size: 8px;
    line-height: 1.45;
    color: var(--muted);
  }
  .contact-line {
    display: flex;
    align-items: center;
    gap: 5px;
  }
  .contact-icon {
    width: 8px;
    height: 8px;
    flex: none;
  }
  .contact-address { margin-top: 4px; }
  .footer-band {
    position: absolute;
    left: 0;
    bottom: 0;
    width: 600px;
    height: 120px;
  }
  .legal {
    position: absolute;
    left: 150px;
    right: 20px;
    bottom: 10px;
    font-size: 7px;
    color: #ffffff;
    text-align: center;
    letter-spacing: 0.2px;
  }
</style>
</head>
<body>
  <main class="letterhead">
    <header class="brand">
      <div class="brand-mark">
        <span class="brand-name">DMB</span>
        <span class="brand-dot"></span>
      </div>
      <p class="brand-firm">Cabinet Durvaux &amp; Associés</p>
      <p class="brand-tagline">Expertise comptable - Audit - Conseil</p>
    </header>

    <address class="contact">
      <div class="contact-line">
        <svg class="contact-icon" viewBox="0 0 8 8"><rect width="8" height="8" rx="1" fill="var(--navy)"/><path d="M2 2.2c0 2 1.8 3.8 3.8 3.8l.4-1-1-.5-.5.5c-.8-.4-1.3-.9-1.7-1.7l.5-.5-.5-1z" fill="#fff"/></svg>
        <span>+689 40 73 16 84</span>
      </div>
      <div class="contact-line">
        <svg class="contact-icon" viewBox="0 0 8 8"><rect width="8" height="8" rx="1" fill="var(--navy)"/><rect x="2" y="3" width="4" height="3" fill="#fff"/><rect x="2.8" y="1.8" width="2.4" height="1.4" fill="#fff"/></svg>
        <span>+689 40 39 57 61</span>
      </div>
      <div class="contact-line">
        <svg class="contact-icon" viewBox="0 0 8 8"><rect width="8" height="8" rx="1" fill="var(--navy)"/><rect x="1.6" y="2.4" width="4.8" height="3.2" fill="#fff"/><path d="M1.6 2.4L4 4.3l2.4-1.9" stroke="var(--navy)" stroke-width=".6" fill="none"/></svg>
        <span>contact@dmb-conseil.pf</span>
      </div>
      <div class="contact-line">
        <svg class="contact-icon" viewBox="0 0 8 8"><rect width="8" height="8" rx="1" fill="var(--navy)"/><circle cx="4" cy="4" r="2.2" stroke="#fff" stroke-width=".6" fill="none"/><path d="M1.8 4h4.4M4 1.8v4.4" stroke="#fff" stroke-width=".5"/></svg>
        <span>www.dmb-conseil.pf</span>
      </div>
      <div class="contact-address">
        <div class="contact-line">
          <svg class="contact-icon" viewBox="0 0 8 8"><rect width="8" height="8" rx="1" fill="var(--navy)"/><path d="M4 1.5a1.8 1.8 0 0 1 1.8 1.8C5.8 4.6 4 6.5 4 6.5S2.2 4.6 2.2 3.3A1.8 1.8 0 0 1 4 1.5z" fill="#fff"/></svg>
          <span>Centre d’affaires OPALE</span>
        </div>
        <div style="padding-left:13px">Rue Gaston Verdier - BP 51839</div>
        <div style="padding-left:13px">MAHANA KOLO - 98713 Papeete</div>
        <div style="padding-left:13px">Tahiti - Polynésie française</div>
      </div>
    </address>

    <svg class="footer-band" viewBox="0 0 600 120" preserveAspectRatio="none" aria-hidden="true">
      <path d="M0 96 C 200 96, 420 80, 600 6 L 600 14 C 420 86, 200 102, 0 104 Z" fill="var(--slate)"/>
      <path d="M0 106 C 200 104, 420 92, 600 20 L 600 120 L 0 120 Z" fill="var(--navy)"/>
    </svg>

    <footer class="legal">Société à responsabilité limitée au capital de 200.000 FCFP - RCS Papeete 58207K - Numéro tahiti K63095</footer>
  </main>
</body>
</html>
```